Business card logo/design needed

I need a new and fresh business card to get my name out there.
I have made plenty before and have a logo but I dont think it is sending the right message across.
I am a personal trainer running a small online business designed to cut the cost of training by taking it online, allowing you to purchase training over the net, through the help of Skype and video uploads.
You can personalized programs hand written for you or more general programs aimed at your goals.
Our goal is to get everyone to look like and behave like an athlete because there is no point in being in shape if you cant do anything with that body.
I also have a strong background in sports, having played low level college basketball in america and worked as a strength and conditioning coach. I dont like running or slow cardio, I am more focused on weights and functional training for aerobic fitness.
I am young for what I do, but I have lot of knowledge and I need something that says that I am not your standard drill sergeant trainer but someone who will truly help you reach your goals.
My curent logo text is "the climb to the top" but I am not set on that.

Industry/Entity Type

Personal Trainer

Contact Information for Business Card

Desmond Quilby
Summit Forge Motion
Personal trainer
Strength and conditioning coach
0481 552 709
www.summitforgemotion.example

```html
<!DOCTYPE html>
<html lang="en">
<head>
<meta charset="utf-8">
<title>Summit Forge Motion – Business Card</title>
<link rel="stylesheet" href="https://fonts.googleapis.com/css2?family=Marcellus&family=Josefin+Sans:wght@300&family=Montserrat:wght@600&display=swap">
<style>
  :root {
    --canvas: #d9d6d2;
    --card-core: #1c1c1c;
    --card-edge: #050505;
    --brand-green: #7fc241;
    --text-light: #e6e6e6;
    --card-w: 680px;
    --card-h: 370px;
  }
  * { margin: 0; padding: 0; box-sizing: border-box; }
  html, body {
    width: 1200px;
    height: 1000px;
    overflow: hidden;
    background: var(--canvas);
  }
  .sheet {
    position: relative;
    width: 1200px;
    height: 1000px;
  }
  .card {
    position: absolute;
    width: var(--card-w);
    height: var(--card-h);
    background: radial-gradient(ellipse at 50% 40%, var(--card-core) 0%, var(--card-edge) 85%);
    box-shadow: 0 6px 18px rgba(0,0,0,0.25);
  }
  .card--front { left: 70px; top: 70px; }
  .card--back { left: 450px; top: 560px; }

  /* Front */
  .brand {
    position: absolute;
    left: 0; right: 0;
    top: 110px;
    display: flex;
    flex-direction: column;
    align-items: center;
  }
  .brand__mark {
    width: 74px;
    height: 74px;
    border-radius: 50%;
    background: var(--brand-green);
    margin-bottom: 34px;
  }
  .brand__name {
    font-family: "Marcellus", serif;
    font-size: 24px;
    letter-spacing: 0.5px;
    color: var(--brand-green);
    text-transform: uppercase;
  }
  .brand__tagline {
    font-family: "Montserrat", sans-serif;
    font-weight: 600;
    font-size: 11px;
    letter-spacing: 2.2px;
    color: var(--text-light);
    text-transform: uppercase;
    margin-top: 4px;
  }

  /* Back */
  .person {
    position: absolute;
    left: 60px;
    top: 148px;
  }
  .person__name {
    font-family: "Marcellus", serif;
    font-size: 33px;
    color: var(--brand-green);
    line-height: 1;
  }
  .person__role {
    font-family: "Montserrat", sans-serif;
    font-weight: 600;
    font-size: 10px;
    letter-spacing: 2.4px;
    color: var(--text-light);
    text-transform: uppercase;
    margin-top: 4px;
  }
  .contact {
    position: absolute;
    left: 375px;
    top: 126px;
    font-family: "Josefin Sans", sans-serif;
    font-weight: 300;
    line-height: 1.3;
  }
  .contact__label {
    font-size: 17px;
    color: var(--brand-green);
  }
  .contact__value {
    font-size: 18px;
    color: var(--text-light);
  }
  .specialty {
    position: absolute;
    left: 0; right: 0;
    top: 282px;
    text-align: center;
    font-family: "Josefin Sans", sans-serif;
    font-weight: 300;
    font-size: 18px;
    color: var(--text-light);
  }
</style>
</head>
<body>
<main class="sheet">
  <section class="card card--front">
    <div class="brand">
      <span class="brand__mark"></span>
      <h1 class="brand__name">Summit Forge Motion</h1>
      <p class="brand__tagline">The climb to the top</p>
    </div>
  </section>

  <section class="card card--back">
    <div class="person">
      <h2 class="person__name">Desmond Quilby</h2>
      <p class="person__role">Personal trainer</p>
    </div>
    <div class="contact">
      <p class="contact__label">Phone:</p>
      <p class="contact__value">0481 552 709</p>
      <p class="contact__label">Web:</p>
      <p class="contact__value">www.summitforgemotion.example</p>
    </div>
    <p class="specialty">Strength and conditioning coach</p>
  </section>
</main>
</body>
</html>
```